ALL TEXT GRAPHICS TM May 2025 for Instagram

We are looking for a series of social media graphics for Instagram (new size: 4:5 (1080 x 1350 pixels) ratio that are ALL TEXT. We want the following quotes below on each graphic; one quote per graphic. AND, In very small letters at the bottom of each graphic, add @TovaMarshOnline
The look and feel of these graphics should be complimentary to the color palette attached below; but keep them simple. But the design is up to you; at the end of this document, I provided various samples of all text graphics that I like as examples.
Target Market(s)
women looking to lose weight
Look and feel

```html
<!DOCTYPE html>
<html lang="en">
<head>
<meta charset="utf-8">
<title>All Text Graphics – Tova Marsh</title>
<link href="https://fonts.googleapis.com/css2?family=Bebas+Neue&family=Montserrat:wght@400;500;600;700;800&display=swap" rel="stylesheet">
<style>
  :root {
    --hot-pink: #ff0a8c;
    --soft-pink: #ff69b4;
    --blush: #fdd3ea;
    --magenta: #d4006a;
    --accent: #f0107f;
    --ink: #141414;
    --white: #ffffff;
  }
  * { box-sizing: border-box; margin: 0; padding: 0; }
  html, body { width: 1200px; height: 1200px; overflow: hidden; background: var(--white); }
  body { position: relative; font-family: "Montserrat", Arial, sans-serif; }

  .post { position: absolute; width: 289px; height: 361px; overflow: hidden; color: var(--white); }
  .post--hot { background: var(--hot-pink); }
  .post--soft { background: var(--soft-pink); }
  .post--blush { background: var(--blush); color: var(--ink); }
  .post--magenta { background: var(--magenta); }

  .ring { position: absolute; left: 30px; top: -12px; width: 24px; height: 24px; border: 4px solid var(--white); border-radius: 50%; }
  .post--blush .ring { border-color: var(--magenta); }

  .brand-mark { position: absolute; right: 22px; top: 22px; font-weight: 700; font-size: 16px; color: var(--white); letter-spacing: 1px; }
  .post--blush .brand-mark { color: var(--accent); }

  .arc-area { position: absolute; left: 124px; bottom: 0; width: 40px; height: 18px; border-radius: 20px 20px 0 0; background: rgba(255,255,255,.22); }
  .post--blush .arc-area { background: rgba(240,16,127,.18); }
  .dot-field { position: absolute; right: 8px; bottom: 6px; width: 56px; height: 62px; background: rgba(255,255,255,.14); }
  .post--blush .dot-field { background: rgba(240,16,127,.12); }

  .copy { position: absolute; left: 27px; right: 18px; }
  .handle { display: flex; align-items: center; gap: 8px; font-size: 9px; font-weight: 500; }
  .handle::after { content: ""; display: block; width: 60px; height: 1px; background: currentColor; }
  .handle--plain::after { display: none; }
  .condensed { font-family: "Bebas Neue", "Arial Narrow", sans-serif; font-weight: 400; }
  .pink { color: var(--accent); }
  .dark { color: var(--ink); }
  .light { color: var(--white); }

  /* Post 1 */
  .frame { position: absolute; left: 6px; top: 96px; width: 277px; height: 177px; border: 2px solid var(--white); }
  .p1 .kicker { font-size: 12px; font-weight: 600; margin-bottom: 8px; }
  .p1 .headline { font-size: 23px; font-weight: 800; line-height: 26px; margin-bottom: 14px; }

  /* Post 2 */
  .card { position: absolute; left: 17px; top: 94px; width: 254px; height: 196px; border: 2px solid var(--white); border-radius: 20px; background: var(--hot-pink); }
  .p2 .kicker { font-size: 14px; font-weight: 700; margin-bottom: 4px; }
  .p2 .headline { font-size: 39px; line-height: 38px; margin-bottom: 10px; letter-spacing: -0.5px; }
  .p2 .body { font-size: 13.5px; line-height: 19px; margin-bottom: 24px; }

  /* Post 3 & 4 */
  .statement { font-size: 22px; font-weight: 700; line-height: 23px; margin-bottom: 14px; }
  .body-lg { font-size: 15.5px; line-height: 21.5px; }

  /* Post 5 */
  .panel-inner { position: absolute; left: 12px; top: 31px; width: 260px; height: 303px; background: var(--blush); }
  .brand-mark--panel { color: var(--accent); right: 30px; top: 44px; }
  .big-caps { font-size: 41px; line-height: 34px; }
  .mid-caps { font-size: 28px; line-height: 30px; margin-top: 4px; }
  .body-md { font-size: 18px; line-height: 25px; }

  /* Post 7, 8, 9 */
  .bold-lines { font-size: 20px; font-weight: 700; line-height: 25.5px; letter-spacing: -0.3px; }

  /* Post 10 */
  .stack { font-size: 32px; line-height: 27px; margin-bottom: 9px; }
</style>
</head>
<body>

<!-- Row 1 -->
<section class="post post--hot" style="left:10px; top:33px;">
  <span class="ring"></span><span class="brand-mark">TM</span>
  <div class="frame"></div>
  <div class="copy p1" style="left:22px; top:121px;">
    <p class="kicker">Tired. Moody. Stubborn Belly Fat.</p>
    <h2 class="headline">YOUR HORMONES ARE SCREAMING FOR HELP!</h2>
    <p class="handle handle--plain">@TovaMarshOnline</p>
  </div>
  <div class="arc-area" role="img" aria-label="Concentric arc ornament"></div>
  <div class="dot-field" role="img" aria-label="Dot grid pattern"></div>
</section>

<section class="post post--soft" style="left:310px; top:33px;">
  <span class="ring"></span><span class="brand-mark">TM</span>
  <div class="card"></div>
  <div class="copy p2" style="left:33px; top:120px;">
    <p class="kicker">THAT STUBBORN WEIGHT?</p>
    <h2 class="headline condensed">IT’S NOT YOUR FAULT.</h2>
    <p class="body">Your <b>hormones</b> are to <b>blame</b> and you’re not alone; <b>But there is a fix.</b></p>
    <p class="handle">@TovaMarshOnline</p>
  </div>
  <div class="arc-area" role="img" aria-label="Concentric arc ornament"></div>
  <div class="dot-field" role="img" aria-label="Dot grid pattern"></div>
</section>

<section class="post post--hot" style="left:609px; top:33px;">
  <span class="ring"></span><span class="brand-mark">TM</span>
  <div class="copy" style="left:42px; top:118px;">
    <h2 class="statement">Your belly isn’t fat…<br>it’s hormonal.</h2>
    <p class="body-lg">And here’s how to <b>fix</b> it. Comment <b>HORMONES</b> if nothing is <b>working.</b></p>
    <p class="handle handle--plain" style="margin-top:20px;">@TovaMarshOnline</p>
  </div>
  <div class="arc-area" role="img" aria-label="Concentric arc ornament"></div>
  <div class="dot-field" role="img" aria-label="Dot grid pattern"></div>
</section>

<section class="post post--hot" style="left:909px; top:33px;">
  <span class="ring"></span><span class="brand-mark">TM</span>
  <div class="copy" style="left:42px; right:12px; top:102px;">
    <h2 class="statement" style="margin-bottom:16px;">The stubborn<br>belly fat after 40?</h2>
    <p class="body-lg">It’s not about <b>calories;</b> it’s about your <b>hormones.</b></p>
    <p class="body-lg" style="font-size:17px; font-weight:600; margin-top:8px;">Here is the fix!</p>
    <p class="handle" style="margin-top:20px;">@TovaMarshOnline</p>
  </div>
  <div class="arc-area" role="img" aria-label="Concentric arc ornament"></div>
  <div class="dot-field" role="img" aria-label="Dot grid pattern"></div>
</section>

<!-- Row 2 -->
<section class="post post--hot" style="left:12px; top:406px;">
  <span class="ring"></span>
  <div class="panel-inner"></div>
  <span class="brand-mark brand-mark--panel">TM</span>
  <div class="copy" style="left:32px; right:38px; top:78px;">
    <h2 class="big-caps condensed pink">FLAT TUMMY<br>IN YOUR 40S?</h2>
    <p class="mid-caps condensed pink">IT’S STILL POSSIBLE!</p>
    <p class="body-md dark" style="margin-top:10px;">Comment <b class="pink">BYE BELLY</b><br>to get the <b class="pink">10 secrets</b> to a <b class="pink">flatter tummy.</b></p>
    <p class="handle handle--plain dark" style="margin-top:22px;">@TovaMarshOnline</p>
  </div>
  <div class="arc-area" role="img" aria-label="Concentric arc ornament"></div>
  <div class="dot-field" role="img" aria-label="Dot grid pattern" style="width:96px; height:14px;"></div>
</section>

<section class="post post--blush" style="left:310px; top:406px;">
  <span class="ring"></span><span class="brand-mark">TM</span>
  <div class="copy" style="top:78px; right:14px;">
    <h2 class="big-caps condensed pink">BLOATING.<br>MUFFIN TOP.<br>PUFFY WAISTLINE.</h2>
    <p class="body-md dark" style="margin-top:10px;">Your body’s screaming<br>for a different kind of fix.</p>
    <p class="body-md pink">Here it is</p>
    <p class="handle pink" style="margin-top:16px;">@TovaMarshOnline</p>
  </div>
  <div class="arc-area" role="img" aria-label="Concentric arc ornament"></div>
  <div class="dot-field" role="img" aria-label="Dot grid pattern"></div>
</section>

<section class="post post--hot" style="left:609px; top:406px;">
  <span class="ring"></span><span class="brand-mark">TM</span>
  <div class="copy dark" style="top:88px; right:40px;">
    <h2 class="bold-lines">You’re doing all the<br><span class="light">“right”</span> things, but<br>your belly won’t <span class="light">go</span><br><span class="light">down?</span></h2>
    <p style="font-size:13px; font-weight:700; margin-top:10px;">Here’s what you haven’t tried.</p>
    <p class="handle light" style="margin-top:30px;">@TovaMarshOnline</p>
  </div>
  <div class="arc-area" role="img" aria-label="Concentric arc ornament"></div>
  <div class="dot-field" role="img" aria-label="Dot grid pattern"></div>
</section>

<section class="post post--blush" style="left:908px; top:406px;">
  <span class="ring"></span><span class="brand-mark">TM</span>
  <div class="copy" style="top:88px; right:30px;">
    <h2 class="bold-lines">This <span class="pink">90-day plan</span><br>helped <span class="pink">women</span> over<br><span class="pink">40 slim</span> down, get a<br>tiny waist and feel<br><span class="pink">sexy</span> again.</h2>
    <p class="pink" style="font-size:16px; font-weight:700; margin-top:12px;">You’re next.</p>
    <p class="handle pink" style="margin-top:12px;">@TovaMarshOnline</p>
  </div>
  <div class="arc-area" role="img" aria-label="Concentric arc ornament"></div>
  <div class="dot-field" role="img" aria-label="Dot grid pattern"></div>
</section>

<!-- Row 3 -->
<section class="post post--magenta" style="left:308px; top:776px;">
  <span class="ring"></span><span class="brand-mark">TM</span>
  <div class="copy" style="top:88px;">
    <h2 class="bold-lines">This is the secret<br>women over 40 are<br>using to get snatched;<br>without starving.<br>Comment SKINNY to<br>get the exact plan.</h2>
    <p class="handle" style="margin-top:20px;">@TovaMarshOnline</p>
  </div>
  <div class="arc-area" role="img" aria-label="Concentric arc ornament"></div>
  <div class="dot-field" role="img" aria-label="Dot grid pattern"></div>
</section>

<section class="post post--magenta" style="left:611px; top:777px;">
  <span class="ring"></span><span class="brand-mark">TM</span>
  <div class="copy" style="top:80px;">
    <h2 class="stack condensed">WHAT WORKED IN YOUR<br>30S WON’T WORK NOW.</h2>
    <p class="stack condensed">HERE’S WHAT<br>ACTUALLY DOES.</p>
    <p class="stack condensed">DROP 30 POUNDS<br>IN 3 MONTHS.</p>
    <p class="handle" style="margin-top:40px;">@TovaMarshOnline</p>
  </div>
  <div class="arc-area" role="img" aria-label="Concentric arc ornament"></div>
  <div class="dot-field" role="img" aria-label="Dot grid pattern"></div>
</section>

</body>
</html>
```